Bluewater Products Flyer

Bluewater Lending Group, Inc.
Licensed Mortgage Company
Serving the DMV since 1997
"You choose Bluewater, we'll carry it home"
We specialize in...
FHA Loans
* Credit Scores as low as 500
* 203K Renovation Loans
Conventional Loans
* As little as 1% Down
* Bank Statement for Self-Employed
Investor Loans
* DSCR, & Fix & Flip
* Commercial & New Construction
Other Programs
* HELOCS & Reverse Mortgages
Call today for a free consultation
(800) 641-2957
www.bluewaterlendhub.com
NMLS #731846

```html
<!DOCTYPE html>
<html lang="en">
<head>
<meta charset="utf-8">
<title>Bluewater Lending Group – Products Flyer</title>
<link rel="stylesheet" href="https://fonts.googleapis.com/css2?family=Hind:wght@400;500;600;700&family=Tinos:wght@700&family=Oswald:wght@600&display=swap">
<style>
  :root{
    --mat:#c8c8c8;
    --paper:#ffffff;
    --navy:#24438b;
    --navy-deep:#1d3a80;
    --gold:#f8c56a;
    --gold-text:#f5b942;
    --sky:#3d8bef;
    --sky-deep:#1552c2;
    --ink:#111111;
    --photo-a:#7d9a5c;
    --photo-b:#c9bfa8;
  }
  *{box-sizing:border-box;margin:0;padding:0}
  html,body{width:937px;height:1200px;overflow:hidden;background:var(--mat)}
  .canvas{position:relative;width:937px;height:1200px;background:var(--mat)}
  .flyer{
    position:absolute;left:136px;top:101px;width:1211px;height:1816px;
    background:var(--paper);transform:scale(0.55);transform-origin:0 0;overflow:hidden;
    font-family:"Hind",Arial,sans-serif;
  }
  .backdrop{position:absolute;inset:0;width:1211px;height:1816px}
  .abs{position:absolute}
  .brand{left:40px;top:110px;display:flex;align-items:center;gap:16px;
    font-weight:700;font-size:52px;color:var(--navy);line-height:1}
  .brand-dot{width:40px;height:40px;border-radius:50%;background:var(--gold)}
  .brand-sub{left:96px;top:176px;font-weight:700;font-size:28px;color:var(--navy);letter-spacing:1px}
  .tagline-top{right:36px;top:130px;width:560px;text-align:center;font-weight:600;font-size:33px;line-height:46px;color:#fff}
  .tagline-top .accent{color:var(--gold-text)}
  .headline{left:20px;top:450px;width:520px;text-align:center;font-family:"Tinos","Times New Roman",serif;
    font-weight:700;color:#fff;font-size:60px;line-height:70px}
  .headline .big{display:block;color:var(--gold-text);font-size:78px;line-height:100px}
  .specialize{left:0;top:898px;width:1211px;text-align:center;font-family:"Tinos","Times New Roman",serif;
    font-weight:700;font-size:90px;color:var(--navy);line-height:120px}
  .card{top:1048px;width:297px;height:411px;background:var(--navy);color:#fff;text-align:center}
  .card-fha{left:113px}.card-conv{left:456px}.card-inv{left:801px}
  .card-icon{position:absolute;left:72px;top:14px;width:152px;height:152px}
  .card-title{position:absolute;left:0;right:0;top:190px;font-weight:600;font-size:24px;color:var(--gold-text);letter-spacing:.3px}
  .card-list{position:absolute;left:0;right:0;top:233px;border-top:2px solid #b99550;list-style:none;padding:0 28px}
  .card-list li{font-size:23px;line-height:32px;padding:10px 0 12px;border-bottom:2px dotted #c9a66b}
  .call{left:48px;top:1570px;font-family:"Tinos","Times New Roman",serif;font-weight:700;font-size:44px;line-height:54px;color:var(--ink)}
  .phone{left:48px;top:1685px;display:flex;align-items:center;gap:12px;font-family:"Oswald",Arial,sans-serif;
    font-weight:600;font-size:64px;color:var(--navy);line-height:1}
  .phone svg{width:52px;height:52px}
  .programs{right:55px;top:1525px;text-align:right;color:#fff}
  .programs h3{font-weight:700;font-size:43px;line-height:50px}
  .programs p{font-size:28px;line-height:40px}
  .contact{right:52px;top:1690px;text-align:right;color:#fff;font-size:38px;line-height:54px;font-weight:500}
</style>
</head>
<body>
<div class="canvas">
  <div class="flyer">
    <svg class="backdrop" viewBox="0 0 1211 1816" aria-hidden="false">
      <defs>
        <linearGradient id="photoTone" x1="0" y1="0" x2="0" y2="1">
          <stop offset="0" stop-color="var(--photo-b)"/>
          <stop offset="1" stop-color="var(--photo-a)"/>
        </linearGradient>
        <linearGradient id="skyBand" x1="0" y1="0" x2="1" y2="0">
          <stop offset="0" stop-color="var(--sky)"/>
          <stop offset="1" stop-color="var(--sky-deep)"/>
        </linearGradient>
      </defs>
      <rect class="hero-band" x="0" y="288" width="1211" height="600" fill="var(--navy)"/>
      <polygon class="top-band" points="710,0 1211,0 1211,288 520,288" fill="var(--navy)"/>
      <polygon class="chevron" points="553,83 655,83 520,288 640,470 560,500 413,288" fill="var(--gold)"/>
      <polygon class="hero-photo" role="img" aria-label="Photo of a smiling family celebrating in front of their new house holding a home for sale sign"
        points="688,288 1211,288 1211,888 821,888 573,470" fill="url(#photoTone)"/>
      <g fill="none" stroke="var(--gold)" stroke-width="2" stroke-dasharray="2 4">
        <line x1="0" y1="366" x2="263" y2="366"/><line x1="0" y1="378" x2="263" y2="378"/><line x1="0" y1="390" x2="263" y2="390"/>
        <line x1="540" y1="812" x2="790" y2="812"/><line x1="540" y1="825" x2="790" y2="825"/><line x1="540" y1="838" x2="790" y2="838"/>
        <line x1="1150" y1="0" x2="1150" y2="88"/><line x1="1162" y1="0" x2="1162" y2="88"/><line x1="1174" y1="0" x2="1174" y2="88"/>
      </g>
      <polygon class="specialize-band" points="37,888 1174,888 1126,1025 90,1025" fill="var(--gold)"/>
      <polygon class="programs-band" points="653,1484 1211,1484 1211,1660 713,1660" fill="url(#skyBand)"/>
      <polygon class="call-band" points="0,1533 652,1533 712,1660 646,1660 596,1793 0,1793" fill="var(--gold)"/>
      <polygon class="contact-band" points="646,1660 1211,1660 1211,1816 548,1816" fill="var(--navy-deep)"/>
    </svg>

    <div class="abs brand"><span class="brand-dot"></span>Bluewater</div>
    <div class="abs brand-sub">LENDING GROUP, INC.</div>

    <p class="abs tagline-top">LICENSED MORTGAGE COMPANY<br><span class="accent">SERVING THE DMV SINCE 1997</span></p>

    <h1 class="abs headline">YOU CHOOSE<span class="big">BLUEWATER,</span>WE'LL CARRY<br>IT HOME</h1>

    <h2 class="abs specialize">WE SPECIALIZE IN...</h2>

    <section class="abs card card-fha">
      <svg class="card-icon" viewBox="0 0 152 152"><circle cx="76" cy="76" r="74" fill="#2a55b0"/><circle cx="76" cy="76" r="66" fill="var(--gold-text)"/><circle cx="76" cy="76" r="59" fill="#fff"/>
        <path d="M46 72 L76 46 L106 72 L100 72 L100 102 L52 102 L52 72Z" fill="#4f7fd6"/><rect x="68" y="80" width="16" height="22" fill="#fff"/></svg>
      <h3 class="card-title">FHA LOANS</h3>
      <ul class="card-list"><li>Credit Scores as<br>low as 500</li><li>203K Renovation Loans</li></ul>
    </section>
    <section class="abs card card-conv">
      <svg class="card-icon" viewBox="0 0 152 152"><circle cx="76" cy="76" r="74" fill="#2a55b0"/><circle cx="76" cy="76" r="66" fill="var(--gold-text)"/><circle cx="76" cy="76" r="59" fill="#fff"/>
        <path d="M62 60 L76 48 L90 60 L90 72 L62 72Z" fill="#4f7fd6"/><rect x="60" y="72" width="32" height="14" rx="3" fill="#4f7fd6"/>
        <path d="M46 100 L62 94 L84 94 Q92 94 104 86 L108 92 Q96 104 84 106 L46 106Z" fill="#4f7fd6"/></svg>
      <h3 class="card-title">CONVENTIONAL LOANS</h3>
      <ul class="card-list"><li>As little as 1% Down</li><li>Bank Statement for<br>Self-Employed</li></ul>
    </section>
    <section class="abs card card-inv">
      <svg class="card-icon" viewBox="0 0 152 152"><circle cx="76" cy="76" r="74" fill="#2a55b0"/><circle cx="76" cy="76" r="66" fill="var(--gold-text)"/><circle cx="76" cy="76" r="59" fill="#fff"/>
        <circle cx="66" cy="64" r="12" fill="#4f7fd6"/><path d="M46 102 Q46 80 66 80 Q82 80 84 96 L84 102Z" fill="#4f7fd6"/>
        <rect x="80" y="78" width="30" height="20" rx="3" fill="#4f7fd6"/><circle cx="95" cy="88" r="5" fill="#fff"/></svg>
      <h3 class="card-title">INVESTOR LOANS</h3>
      <ul class="card-list"><li>DSCR, &amp; Fix &amp; Flip</li><li>Commercial &amp; New<br>Construction</li></ul>
    </section>

    <p class="abs call">CALL TODAY FOR A FREE<br>CONSULTATION</p>
    <p class="abs phone">
      <svg viewBox="0 0 24 24"><path d="M6.6 10.8a15.1 15.1 0 0 0 6.6 6.6l2.2-2.2a1 1 0 0 1 1-.25 11.4 11.4 0 0 0 3.6.57 1 1 0 0 1 1 1V20a1 1 0 0 1-1 1A17 17 0 0 1 3 4a1 1 0 0 1 1-1h3.5a1 1 0 0 1 1 1c0 1.25.2 2.45.57 3.57a1 1 0 0 1-.25 1Z" fill="var(--navy)"/></svg>
      (800) 641-2957
    </p>

    <div class="abs programs"><h3>OTHER PROGRAMS</h3><p>HELOCS &amp; Reverse Mortgages</p></div>
    <p class="abs contact">www.bluewaterlendhub.com<br>NMLS #731846</p>
  </div>
</div>
</body>
</html>
```